K.T.L Electrical Services Pty Ltd

Electrical contracting business. I have a base for the design which i like. The contact number needs to be changed to 0491736250 and the O made more solid and level with the rest of the letters. If you have any other ideas of what would make it better I'm happy to see them.

The back side to be written as dot points with the following:
- Residential & Commercial
- Maintenance
- PV & Battery servicing
- EV Chargers

```html
<!DOCTYPE html>
<html lang="en">
<head>
<meta charset="UTF-8">
<title>K.T.L Electrical Services – Business Card</title>
<link href="https://fonts.googleapis.com/css2?family=Montserrat:wght@400;500;600;700&display=swap" rel="stylesheet">
<style>
  :root {
    --backdrop: #959595;
    --card: #181818;
    --accent: #8eaeb0;
    --text-light: #ffffff;
    --faint-mark: #1f2020;
  }
  * { box-sizing: border-box; margin: 0; padding: 0; }
  html, body {
    width: 1200px; height: 1000px; overflow: hidden;
    background: var(--backdrop);
    font-family: "Montserrat", sans-serif;
  }
  .card {
    position: absolute;
    width: 650px; height: 375px;
    background: var(--card);
    border-radius: 24px;
    overflow: hidden;
  }
  .card--front { left: 276px; top: 103px; }
  .card--back  { left: 279px; top: 522px; }

  /* Front */
  .front-brand {
    position: absolute; left: 0; right: 0; top: 52px;
    text-align: center; color: var(--accent);
  }
  .front-brand .brand-name {
    font-size: 146px; font-weight: 600; line-height: 1;
    letter-spacing: 2px;
  }
  .front-brand .brand-tagline {
    margin-top: 10px;
    font-size: 31px; font-weight: 500; letter-spacing: 1.5px; line-height: 1;
  }
  .service-list {
    position: absolute; left: 30px; right: 30px; top: 289px;
    text-align: center; list-style: none;
    color: var(--text-light); font-size: 17px; font-weight: 500; line-height: 29px;
  }
  .service-list li { display: inline; }
  .service-list li + li::before {
    content: "•"; color: var(--accent); margin: 0 7px 0 6px;
  }
  .service-list .wrap-line { display: block; }
  .service-list .wrap-line::before { margin-left: 0; }

  /* Back */
  .faint-disc {
    position: absolute; left: 7px; top: 50px;
    width: 298px; height: 298px; border-radius: 50%;
    background: var(--faint-mark);
  }
  .back-details {
    position: absolute; right: 33px; top: 38px;
    text-align: right;
  }
  .back-details .brand-name {
    color: var(--accent); font-size: 84px; font-weight: 600; line-height: 1;
    letter-spacing: 1px;
  }
  .back-details .brand-tagline {
    color: var(--accent); font-size: 16.5px; font-weight: 500; letter-spacing: 0.8px;
    margin-top: 6px; line-height: 1;
  }
  .back-details .licence {
    color: var(--accent); font-size: 13px; font-weight: 500; letter-spacing: 0.6px;
    margin-top: 6px; line-height: 1;
  }
  .person {
    position: absolute; right: 33px; top: 210px; text-align: right;
  }
  .person .person-name {
    color: var(--accent); font-size: 23px; font-weight: 700; letter-spacing: 0.5px; line-height: 1;
  }
  .person .person-role {
    color: var(--text-light); font-size: 16px; margin-top: 10px; line-height: 1;
  }
  .contact {
    position: absolute; right: 33px; top: 288px; text-align: right;
    list-style: none; color: var(--text-light); font-size: 17px; line-height: 29px;
    letter-spacing: 0.5px;
  }
  .contact li { display: flex; justify-content: flex-end; align-items: center; gap: 9px; }
  .contact svg { width: 16px; height: 14px; fill: var(--accent); }
</style>
</head>
<body>
  <section class="card card--front">
    <div class="front-brand">
      <div class="brand-name">K.T.L</div>
      <div class="brand-tagline">ELECTRICAL SERVICES P/L</div>
    </div>
    <ul class="service-list">
      <li>Residential &amp; Commercial</li><li>Maintenance</li><li>PV &amp; Battery servicing</li><li class="wrap-line">EV Chargers</li>
    </ul>
  </section>

  <section class="card card--back">
    <div class="faint-disc"></div>
    <div class="back-details">
      <div class="brand-name">K.T.L</div>
      <div class="brand-tagline">ELECTRICAL SERVICES P/L</div>
      <div class="licence">EC 20417</div>
    </div>
    <div class="person">
      <div class="person-name">DANIEL HARLOW</div>
      <div class="person-role">Owner</div>
    </div>
    <ul class="contact">
      <li>049 173 6250
        <svg viewBox="0 0 16 14" aria-hidden="true"><path d="M1 4c0-2 3-3 7-3s7 1 7 3v1.5h-3.5V4H4.5v1.5H1z"/><path d="M4 6h8l2 7H2z"/></svg>
      </li>
      <li>info@ktlelectrical.com
        <svg viewBox="0 0 16 14" aria-hidden="true"><path d="M0 2h16v10H0z" /><path d="M0 2l8 6 8-6" fill="none" stroke="#181818" stroke-width="1.4"/></svg>
      </li>
    </ul>
  </section>
</body>
</html>
```